Commercial Swimming Pool - Design-Build Contractor Website Design

I need a new website that will feature our newly developed logo and trade name as well as provide a fully updated site experience. We are not a residential builder - we strictly design and install high-end commercial pools. I need the website to highlight our portfolio and communicate the various types of projects in which we specialize. I want the effect of the site to reflect the high-end nature of our services - projects like the 57th floor spa at the Wrenport Halvard Towers, the aquatic therapy portion of the Wrenport Gale Runners training facility, a 5om indoor competition pool for the prestigious Dunlowe Preparatory, the indoor water park at The Caskwell Inn or the recent country club renovation projects we've completed in our region (to name a few examples).

```html
<!DOCTYPE html>
<html lang="en">
<head>
<meta charset="utf-8">
<title>Velmora Aquatics — Commercial Pool Design-Build</title>
<link rel="stylesheet" href="https://fonts.googleapis.com/css2?family=Open+Sans:wght@400;600;700&family=Roboto:wght@400;500&display=swap">
<style>
:root{
  --navy:#1c1f5f;
  --navy-deep:#161a52;
  --sky:#3fb2e4;
  --sky-soft:#e9f0fb;
  --gray-bg:#f1f1f4;
  --text:#2b2f6b;
  --muted:#6b6f8a;
  --white:#ffffff;
  --star:#f5b400;
}
*{margin:0;padding:0;box-sizing:border-box}
html,body{width:1200px;height:4608px;overflow:hidden;background:var(--white)}
body{font-family:"Open Sans",sans-serif;color:var(--text)}
.page{position:relative;width:1200px;height:4608px;overflow:hidden}
.abs{position:absolute}
.btn{position:absolute;display:flex;align-items:center;justify-content:center;background:var(--sky);color:var(--white);font-weight:600;font-size:13px;border-radius:3px}
.label{position:absolute;font-size:10px;font-weight:600;color:var(--sky);letter-spacing:.3px;display:flex;align-items:center;gap:12px}
.label i{display:block;width:50px;height:2px;background:var(--sky)}
.h2{position:absolute;font-weight:700;color:var(--navy);font-size:44px;line-height:60px}
.center{left:0;width:1200px;text-align:center;justify-content:center}
/* header */
.header{position:absolute;left:0;top:0;width:1200px;height:148px;background:#f6f8fd}
.brand{position:absolute;left:93px;top:38px;display:flex;align-items:center;gap:10px;font-weight:700;font-size:24px;color:var(--navy);letter-spacing:1px}
.brand .mark{width:40px;height:40px;border-radius:50%;background:var(--sky)}
.info{position:absolute;top:40px;display:flex;gap:14px;font-family:"Roboto",sans-serif;font-size:12px;color:#555;line-height:20px}
.info .ic{width:36px;height:36px;border-radius:50%;background:var(--white);display:flex;align-items:center;justify-content:center;margin-top:4px}
.info small{display:block;font-size:12px;color:#888}
.navbar{position:absolute;left:254px;top:114px;width:880px;height:51px;background:var(--white);border-radius:26px;box-shadow:0 3px 10px rgba(0,0,0,.08);display:flex;align-items:center;padding-left:90px;gap:31px;font-family:"Roboto",sans-serif;font-size:13px;color:#333}
.navbar .appt{position:absolute;right:0;top:4px;width:158px;height:47px;border-radius:24px;background:var(--sky);color:var(--white);display:flex;align-items:center;justify-content:center;border:3px solid #fff;box-shadow:0 2px 6px rgba(0,0,0,.15)}
/* hero */
.hero-photo{position:absolute;left:0;top:148px;width:1200px;height:712px;background:linear-gradient(160deg,#5b5f66 0%,#3c4047 40%,#2d4150 70%,#4a6b7a 100%)}
.hero-kicker{position:absolute;left:82px;top:358px;color:#fff;font-family:"Roboto",sans-serif;font-size:18px}
.hero-title{position:absolute;left:72px;top:400px;color:#fff;font-size:66px;line-height:86px;font-weight:600}
/* about */
.about-ring{position:absolute;left:98px;top:937px;width:440px;height:440px;border-radius:50%;border:2px solid var(--navy)}
.about-photo{position:absolute;left:112px;top:952px;width:412px;height:412px;border-radius:50%;background:linear-gradient(135deg,#c9b89c 0%,#7fb7d9 45%,#2d9be0 100%)}
.about-badge{position:absolute;left:353px;top:1179px;width:196px;height:196px;border-radius:50%;background:#2f3a66}
.about-text{position:absolute;left:615px;font-size:13px;line-height:24px;color:var(--text);width:470px}
/* services */
.services{position:absolute;left:0;top:1477px;width:1200px;height:713px;background:var(--gray-bg)}
.arrow-box{position:absolute;width:43px;height:62px;background:#fff;display:flex;align-items:center;justify-content:center;box-shadow:0 2px 6px rgba(0,0,0,.08)}
.svc-card{position:absolute;top:1702px;width:322px;height:313px;border-radius:6px;overflow:hidden}
.svc-card .ico{position:absolute;left:32px;top:39px;width:86px;height:86px;border-radius:50%;background:var(--sky);display:flex;align-items:center;justify-content:center}
.svc-card h3{position:absolute;left:32px;top:146px;color:#fff;font-size:22px;font-weight:600}
.svc-card p{position:absolute;left:32px;top:212px;color:#fff;font-size:13px}
.svc-card .more{position:absolute;left:32px;top:250px;color:#fff;font-size:15px;font-weight:700}
.svc-card .line{position:absolute;left:32px;right:32px;top:280px;height:1px;background:rgba(255,255,255,.6)}
/* banner */
.banner{position:absolute;left:0;top:2190px;width:1200px;height:361px;background:linear-gradient(100deg,#2d3a7a 0%,#3b4a8f 50%,#34427f 100%)}
.banner-title{position:absolute;left:97px;top:2270px;color:#fff;font-size:44px;line-height:60px;font-weight:600}
.banner-text{position:absolute;left:97px;top:2412px;color:#fff;font-size:12.5px;line-height:24px;width:640px}
.ghost{position:absolute;left:937px;width:168px;height:45px;border-radius:4px;display:flex;align-items:center;justify-content:center;gap:8px;font-size:13px;font-weight:600}
/* projects */
.proj{position:absolute;top:2750px;height:400px;border-radius:10px}
.caption{position:absolute;left:240px;top:3034px;width:715px;height:77px;background:#fff;display:flex;align-items:center;padding-left:16px;font-size:16px;font-weight:600;color:var(--navy);white-space:nowrap}
.caption .go{position:absolute;right:0;top:0;width:79px;height:77px;background:var(--navy);display:flex;align-items:center;justify-content:center}
/* testimonials */
.testi-bg{position:absolute;left:0;top:3228px;width:1200px;height:1380px;background:var(--gray-bg)}
.t-card{position:absolute;top:3442px;width:320px;height:223px;background:#fff;box-shadow:0 2px 8px rgba(0,0,0,.06)}
.t-card .avatar{position:absolute;right:32px;top:-28px;width:96px;height:96px;border-radius:50%;background:#e3e6ee;border:6px solid #fff}
.t-card .avatar::after{content:"";position:absolute;inset:8px;border-radius:50%;background:linear-gradient(160deg,#9fb7c9,#5f7a93)}
.t-card .quote{position:absolute;right:24px;top:-32px;width:36px;height:36px;border-radius:50%;background:var(--navy);color:#fff;font-size:20px;font-weight:700;display:flex;align-items:center;justify-content:center}
.t-card .stars{position:absolute;left:29px;top:44px;color:var(--star);font-size:18px;letter-spacing:1px}
.t-card p{position:absolute;left:29px;top:78px;width:268px;font-size:12.5px;line-height:21px;color:#444}
.t-card .name{position:absolute;left:29px;top:172px;font-size:17px;font-weight:700;color:var(--navy)}
.t-card .name small{font-size:11px;font-weight:400;color:#888;margin-left:4px}
/* contact */
.contact-card{position:absolute;left:164px;top:3871px;width:875px;height:456px;background:#fff;box-shadow:0 4px 14px rgba(0,0,0,.06)}
.contact-card .topline{position:absolute;left:40px;top:0;width:794px;height:4px;background:#4f6b78}
.field{position:absolute;left:52px;width:347px;background:var(--sky-soft);font-size:12px;color:#666;padding:14px 14px}
.c-row{position:absolute;display:flex;gap:20px;font-size:13px;color:#333;line-height:25px}
.c-row .ci{width:32px;height:32px;border-radius:50%;background:var(--navy);display:flex;align-items:center;justify-content:center;flex-shrink:0}
/* footer */
.f-brand{position:absolute;left:283px;top:4386px;color:#fff;font-size:24px;font-weight:700;letter-spacing:1px}
.f-item{position:absolute;top:4380px;display:flex;gap:14px;color:#fff;font-size:13px;line-height:19px}
.f-nav{position:absolute;left:256px;top:4468px;width:706px;height:55px;border-top:1px solid rgba(255,255,255,.5);border-bottom:1px solid rgba(255,255,255,.5);display:flex;align-items:center;justify-content:space-between;padding:0 20px;color:#fff;font-size:13px}
.copy{position:absolute;left:147px;top:4566px;color:#fff;font-size:11px}
.social{position:absolute;top:4562px;width:26px;height:26px;border:1px solid #fff}
</style>
</head>
<body>
<div class="page">

  <header class="header">
    <div class="brand"><span class="mark"></span>VELMORA AQUATICS</div>
    <div class="info" style="left:425px">
      <span class="ic"><svg width="16" height="16" viewBox="0 0 24 24" fill="none" stroke="#3fb2e4" stroke-width="2"><path d="M5 3h4l2 5-3 2a12 12 0 0 0 6 6l2-3 5 2v4a2 2 0 0 1-2 2A18 18 0 0 1 3 5a2 2 0 0 1 2-2z"/></svg></span>
      <div><small>Phone Number</small>+123 456 7890</div>
    </div>
    <div class="info" style="left:670px">
      <span class="ic"><svg width="16" height="16" viewBox="0 0 24 24" fill="none" stroke="#3fb2e4" stroke-width="2"><rect x="3" y="5" width="18" height="14" rx="2"/><path d="M3 7l9 6 9-6"/></svg></span>
      <div><small>Email Address</small>company@example.com</div>
    </div>
    <div class="info" style="left:915px">
      <span class="ic"><svg width="16" height="16" viewBox="0 0 24 24" fill="#3fb2e4"><path d="M12 2a7 7 0 0 0-7 7c0 5 7 13 7 13s7-8 7-13a7 7 0 0 0-7-7zm0 9.5A2.5 2.5 0 1 1 12 6a2.5 2.5 0 0 1 0 5.5z"/></svg></span>
      <div><small>Location</small>123 Rd Country</div>
    </div>
    <nav class="navbar">
      <span>Home</span><span>About Us</span><span>Services</span><span>Gallery</span><span>Blog</span><span>Contact Us</span>
      <span class="appt">Appointment</span>
    </nav>
  </header>

  <div class="hero-photo" role="img" aria-label="Rooftop pool at dusk overlooking a city skyline"></div>
  <svg class="abs" style="left:0;top:740px" width="1200" height="130" viewBox="0 0 1200 130">
    <path d="M0 63 C250 85 520 140 820 125 C1010 115 1130 80 1200 20 L1200 130 L0 130 Z" fill="#fff"/>
  </svg>
  <div class="hero-kicker">COMMERCIAL POOL CONSTRUCTION</div>
  <h1 class="hero-title">Designing pools that fit<br>your budget and style</h1>
  <div class="btn" style="left:79px;top:597px;width:159px;height:56px;border-radius:28px;font-weight:400;font-family:Roboto,sans-serif;font-size:14px">Read More</div>

  <div class="about-ring"></div>
  <div class="about-photo" role="img" aria-label="Technician servicing a pool ladder beside blue water"></div>
  <div class="about-badge"></div>
  <div class="label" style="left:615px;top:966px">ABOUT US <i></i></div>
  <h2 class="h2" style="left:614px;top:996px">Dive into quality Pool<br>construction with us</h2>
  <p class="about-text" style="top:1130px">Lorem ipsum dolor sit amet, consectetur adipiscing elit, sed do eiusmo empor incididunt ut abore et dolore magna aliqua. Ut enim ad minim iam, quis nostrud exercitation ullamco</p>
  <p class="about-text" style="top:1213px">Lorem ipsum dolor sit amet, consectetur adipiscing elit, sed do eiusmo empor incididunt ut abore et dolore magna aliqua. Ut enim ad minim iam, quis nostrud exercitation ullamco</p>
  <div class="btn" style="left:615px;top:1320px;width:168px;height:46px">Contact Us</div>

  <section class="services"></section>
  <div class="label" style="left:89px;top:1563px">SERVICES <i></i></div>
  <h2 class="h2" style="left:88px;top:1595px">Services We Offer</h2>
  <div class="arrow-box" style="left:1001px;top:1579px"><svg width="12" height="18" viewBox="0 0 12 18"><path d="M9 2L3 9l6 7" fill="none" stroke="#222" stroke-width="2"/></svg></div>
  <div class="arrow-box" style="left:1053px;top:1579px"><svg width="12" height="18" viewBox="0 0 12 18"><path d="M3 2l6 7-6 7" fill="none" stroke="#222" stroke-width="2"/></svg></div>

  <div class="svc-card" style="left:91px;background:linear-gradient(180deg,#4f9bd0 0%,#3c6f55 45%,#5aa7c4 100%)" role="img" aria-label="Resort pool bordered by hedges">
    <span class="ico"><svg width="40" height="40" viewBox="0 0 40 40" fill="none" stroke="#fff" stroke-width="2"><path d="M6 24c4-3 7 3 11 0s7 3 11 0 6 2 6 2M6 31c4-3 7 3 11 0s7 3 11 0 6 2 6 2M14 20V8a3 3 0 0 1 6 0M24 20V10"/></svg></span>
    <h3>Pool Construction</h3><p>Lorem ipsum dolor sit amet, consectetur</p><span class="more">Read More</span><span class="line"></span>
  </div>
  <div class="svc-card" style="left:438px;background:linear-gradient(180deg,#9aa3a8 0%,#5f6a5d 55%,#7c8a4a 100%)" role="img" aria-label="Site engineer in hard hat and safety vest">
    <span class="ico"><svg width="40" height="40" viewBox="0 0 40 40" fill="none" stroke="#fff" stroke-width="2"><path d="M11 17a9 9 0 0 1 18 0H11zM20 8v4M13 21a7 7 0 0 0 14 0M10 34c2-5 6-7 10-7s8 2 10 7"/></svg></span>
    <h3>Pool Servicing</h3><p>Lorem ipsum dolor sit amet, consectetur</p><span class="more">Read More</span><span class="line"></span>
  </div>
  <div class="svc-card" style="left:787px;background:linear-gradient(160deg,#c9d7df 0%,#a8c4d2 50%,#d9c3a6 100%)" role="img" aria-label="Hand sketching a pool plan with a ruler">
    <span class="ico"><svg width="40" height="40" viewBox="0 0 40 40" fill="none" stroke="#fff" stroke-width="2"><circle cx="13" cy="13" r="5"/><path d="M17 17l14 14M27 9l4 4-14 14-4-4zM9 27l4 4"/></svg></span>
    <h3>Pool Design</h3><p>Lorem ipsum dolor sit amet, consectetur</p><span class="more">Read More</span><span class="line"></span>
  </div>
  <div class="btn" style="left:513px;top:2087px;width:168px;height:46px">Contact Us</div>

  <section class="banner" role="img" aria-label="Smiling construction team in hard hats, tinted blue"></section>
  <h2 class="banner-title">Innovative designs for<br>unique pools</h2>
  <p class="banner-text">Lorem ipsum dolor sit amet, consectetur adipiscing elit, sed do eiusmoempor incididunt ut abore et dolore magna aliqua. Ut enim ad minim iam</p>
  <svg class="abs" style="left:788px;top:2283px" width="14" height="180" viewBox="0 0 14 180"><line x1="4" y1="0" x2="4" y2="180" stroke="#fff" stroke-width="2"/><path d="M4 84l6 6-6 6z" fill="#fff"/></svg>
  <div class="ghost" style="top:2319px;border:2px solid #fff;color:#fff"><svg width="14" height="14" viewBox="0 0 24 24" fill="#fff"><path d="M5 3h4l2 5-3 2a12 12 0 0 0 6 6l2-3 5 2v4a2 2 0 0 1-2 2A18 18 0 0 1 3 5a2 2 0 0 1 2-2z"/></svg>+123 456 789</div>
  <div class="ghost" style="top:2385px;background:#fff;color:var(--navy)">Contact Us</div>

  <div class="label center" style="top:2609px"><i></i>OUR PORTFOLIO<i></i></div>
  <h2 class="h2 center" style="top:2634px">Our Latest Projects</h2>
  <div class="proj" style="left:0;width:179px;border-radius:0 10px 10px 0;background:linear-gradient(160deg,#2f5fb0,#a33a33 60%,#c9b39a)" role="img" aria-label="Worker in blue hard hat and plaid shirt"></div>
  <div class="proj" style="left:220px;width:755px;background:linear-gradient(180deg,#cfdff0 0%,#a9bfe0 45%,#6d8fc7 75%,#2f6fb8 100%)" role="img" aria-label="Aquatic therapy pool between white buildings with a palm tree"></div>
  <div class="proj" style="left:1012px;width:188px;border-radius:10px 0 0 10px;background:linear-gradient(180deg,#4ab7e0 0%,#8fd3ea 45%,#5b4a40 60%,#3e322b 100%)" role="img" aria-label="Pool edge with wooden decking"></div>
  <div class="arrow-box" style="left:91px;top:2911px;width:66px;height:95px"><svg width="14" height="22" viewBox="0 0 14 22"><path d="M11 2L3 11l8 9" fill="none" stroke="#222" stroke-width="2"/></svg></div>
  <div class="arrow-box" style="left:1035px;top:2911px;width:66px;height:95px"><svg width="14" height="22" viewBox="0 0 14 22"><path d="M3 2l8 9-8 9" fill="none" stroke="#222" stroke-width="2"/></svg></div>
  <div class="caption">aquatic therapy portion of Wrenport Gale Runners training facility
    <span class="go"><svg width="30" height="16" viewBox="0 0 30 16" fill="none" stroke="#fff" stroke-width="2"><path d="M0 8h28M21 1l7 7-7 7"/></svg></span></div>

  <div class="testi-bg"></div>
  <div class="label" style="left:89px;top:3273px">TESTIMONIALS <i></i></div>
  <h2 class="h2" style="left:88px;top:3306px">What our clients are saying</h2>
  <div class="arrow-box" style="left:1001px;top:3290px;height:59px"><svg width="12" height="18" viewBox="0 0 12 18"><path d="M9 2L3 9l6 7" fill="none" stroke="#222" stroke-width="2"/></svg></div>
  <div class="arrow-box" style="left:1053px;top:3290px;height:59px"><svg width="12" height="18" viewBox="0 0 12 18"><path d="M3 2l6 7-6 7" fill="none" stroke="#222" stroke-width="2"/></svg></div>

  <div class="t-card" style="left:93px">
    <span class="avatar" role="img" aria-label="Client portrait"></span><span class="quote">❞</span>
    <div class="stars">★★★★★</div>
    <p>Lorem ipsum dolor sit amet, consectetur adipiscing elit, sed do eiusmod tempor in cididunt ut labore et dolore magna a iqua. Ut enim ad</p>
    <div class="name">Alan Smith<small>(Client)</small></div>
  </div>
  <div class="t-card" style="left:437px">
    <span class="avatar" role="img" aria-label="Client portrait"></span><span class="quote">❞</span>
    <div class="stars">★★★★★</div>
    <p>Lorem ipsum dolor sit amet, consectetur adipiscing elit, sed do eiusmod tempor in cididunt ut labore et dolore magna a iqua. Ut enim ad</p>
    <div class="name">Alan Smith<small>(Client)</small></div>
  </div>
  <div class="t-card" style="left:781px">
    <span class="avatar" role="img" aria-label="Client portrait"></span><span class="quote">❞</span>
    <div class="stars">★★★★★</div>
    <p>Lorem ipsum dolor sit amet, consectetur adipiscing elit, sed do eiusmod tempor in cididunt ut labore et dolore magna a iqua. Ut enim ad</p>
    <div class="name">Alan Smith<small>(Client)</small></div>
  </div>
  <div class="abs" style="left:554px;top:3702px;width:34px;height:4px;background:var(--navy)"></div>
  <div class="abs" style="left:595px;top:3702px;width:18px;height:4px;background:#cfd1da"></div>
  <div class="abs" style="left:619px;top:3702px;width:18px;height:4px;background:#cfd1da"></div>

  <div class="label center" style="top:3760px"><i></i>CONTACT<i></i></div>
  <h2 class="h2 center" style="top:3784px">Get in touch with us</h2>
  <svg class="abs" style="left:0;top:4060px" width="1200" height="548" viewBox="0 0 1200 548">
    <path d="M0 80 C60 40 120 20 200 10 L1000 10 C1080 40 1150 70 1200 100 L1200 548 L0 548 Z" fill="#161a52"/>
  </svg>
  <div class="contact-card">
    <span class="topline"></span>
    <h3 class="abs" style="left:52px;top:48px;font-size:29px;line-height:36px;font-weight:600;color:var(--navy)">Feel free to write us<br>for any type of</h3>
    <div class="field" style="top:136px;height:43px">Full Name</div>
    <div class="field" style="top:188px;height:43px">Enter Email address</div>
    <div class="field" style="top:241px;height:72px">Your Messages</div>
    <div class="btn" style="left:52px;top:334px;width:188px;height:47px;font-size:15px;font-weight:700;border-radius:0">SUBMIT NOW</div>
    <span class="abs" style="left:456px;top:16px;width:1px;height:420px;background:#e3e4ea"></span>
    <div class="c-row" style="top:60px;left:482px"><span class="ci"><svg width="14" height="14" viewBox="0 0 24 24" fill="#fff"><path d="M12 2a7 7 0 0 0-7 7c0 5 7 13 7 13s7-8 7-13a7 7 0 0 0-7-7z"/></svg></span><div>Velmora Aquatics<br>ABC Road<br>ABC City<br>ABC Country</div></div>
    <div class="c-row" style="top:178px;left:482px"><span class="ci"><svg width="14" height="14" viewBox="0 0 24 24" fill="#fff"><path d="M5 3h4l2 5-3 2a12 12 0 0 0 6 6l2-3 5 2v4a2 2 0 0 1-2 2A18 18 0 0 1 3 5a2 2 0 0 1 2-2z"/></svg></span><div style="padding-top:4px">123 - 456 - 7890</div></div>
    <div class="c-row" style="top:234px;left:482px"><span class="ci"><svg width="14" height="14" viewBox="0 0 24 24" fill="none" stroke="#fff" stroke-width="2"><rect x="3" y="5" width="18" height="14" rx="2"/><path d="M3 7l9 6 9-6"/></svg></span><div style="padding-top:4px">contactus@company.com</div></div>
    <div class="c-row" style="top:286px;left:482px"><span class="ci"><svg width="14" height="14" viewBox="0 0 24 24" fill="#fff"><path d="M5 5l7 7-7 7zM12 5l7 7-7 7z"/></svg></span><div style="padding-top:4px">8 am - 5pm&nbsp; Mon - Fri</div></div>
    <div class="abs" style="left:492px;top:350px;font-size:13px;color:#333">Reach us here:</div>
  </div>

  <div class="f-brand">VELMORA</div>
  <div class="f-item" style="left:434px"><svg width="28" height="28" viewBox="0 0 24 24" fill="none" stroke="#fff" stroke-width="1.4"><circle cx="12" cy="12" r="10"/><path d="M2 12h20M12 2c3 3 3 17 0 20M12 2c-3 3-3 17 0 20"/></svg><div>123, Building Name, Street<br>City, State XY 123456</div></div>
  <div class="f-item" style="left:688px"><svg width="24" height="30" viewBox="0 0 24 30" fill="none" stroke="#fff" stroke-width="1.6"><rect x="5" y="2" width="14" height="26" rx="2"/><path d="M10 24h4"/></svg><div>PHONE<br>(123) 456 7890</div></div>
  <div class="f-item" style="left:865px"><svg width="28" height="28" viewBox="0 0 24 24" fill="none" stroke="#fff" stroke-width="1.4"><path d="M3 10l9-7 9 7v10H3z"/><path d="M3 10l9 6 9-6"/></svg><div>EMAIL<br>info@company.com</div></div>
  <span class="abs" style="left:413px;top:4378px;width:1px;height:36px;background:rgba(255,255,255,.5)"></span>
  <span class="abs" style="left:667px;top:4378px;width:1px;height:36px;background:rgba(255,255,255,.5)"></span>
  <span class="abs" style="left:844px;top:4378px;width:1px;height:36px;background:rgba(255,255,255,.5)"></span>
  <nav class="f-nav"><span>HOME</span><span>SERVICES</span><span>ABOUT US</span><span>TESTIMONIALS</span><span>BLOG</span><span>CONTACT US</span></nav>
  <div class="copy">All Rights Reserved. 2023</div>
  <span class="social" style="left:932px"></span>
  <span class="social" style="left:965px"></span>
  <span class="social" style="left:998px"></span>
  <span class="social" style="left:1031px"></span>

</div>
</body>
</html>
```